Poster Needed for Church Conference

I need a poster for a weekend conference at my church. Looking to attract as many people as possible. We are a church in the suburbs of Houston. This is mainly for our own church members but we are opening it up to outside church members.

Please see previous design from last conference and all other graphic work that can (doesn't need to be) included.

Target Market(s)

It's targeted for all people. But our main audience is families. around the age of 30 should be main target.

Industry/Entity Type

Non-Profit

Font styles to use
Serif
Sans Serif

Colors

Designer to choose colors to be used in the design.

Requirements
Must have
• 11x17 design with ability to shrink and blow up. but ideally for 11x17
• Content and wording:
• "Rooted Lantern Conference: Bridging the gap between generations and passing on our deepest beliefs and values."
• Featuring Dr. Glen Marlowe. Author of "The Map of Q9"
• Aug 25-26: Friday 8-10 pm, Saturday 4-8 pm
• Cost Adults $15/Children $5: Covers admission to all sessions and workshops, refreshments and Saturday dinner. *kids 5 and under free
• Childcare provided for all sessions. "
• Please use church logo and address on flyer: 4312 Orchard Bend, Cedar Hollow, TX 77512
Nice to have
• Ideally it will be designed so that we can crop a 16:9 pp announcement slide and header for our website.
Should not have
• anything offensive

```html
<!DOCTYPE html>
<html lang="en">
<head>
<meta charset="utf-8">
<title>Rooted Lantern Conference Poster</title>
<link href="https://fonts.googleapis.com/css2?family=Baloo+2:wght@700;800&family=Arvo:wght@400;700&family=Montserrat:wght@700;800&display=swap" rel="stylesheet">
<style>
  :root {
    --charcoal: #3a3a3c;
    --green: #5fbf4e;
    --green-light: #74c865;
    --green-deep: #4aa83c;
    --title-green: #57c248;
    --sky: #2f9be0;
    --sky-dark: #1f78be;
    --white: #ffffff;
    --ink: #2b2b2b;
  }
  * { margin: 0; padding: 0; box-sizing: border-box; }
  html, body { width: 800px; height: 1200px; overflow: hidden; background: #ececec; }
  .poster {
    position: relative; width: 800px; height: 1200px; overflow: hidden;
    background: radial-gradient(circle at 55% 58%, var(--green-light), var(--green) 70%);
  }
  .header-wave { position: absolute; left: 0; top: 0; width: 800px; height: 470px; }
  .headline {
    position: absolute; left: 0; top: 50px; width: 800px; text-align: center;
    font-family: "Baloo 2", sans-serif; color: var(--title-green); font-weight: 800;
  }
  .headline .event-name { font-size: 38px; line-height: 46px; display: block; }
  .headline .tagline { font-size: 54px; line-height: 62px; display: block; margin-top: 10px; }
  .book-cover {
    position: absolute; left: 88px; top: 440px; width: 140px; height: 195px;
    background: linear-gradient(160deg, #ffffff, #dcdcdc);
    transform: rotate(-8deg); box-shadow: 4px 6px 10px rgba(0,0,0,.3);
  }
  .speaker-photo {
    position: absolute; left: 481px; top: 434px; width: 268px; height: 315px;
    border: 3px solid var(--white); border-radius: 10px;
    background: linear-gradient(160deg, #2a2a2a, #5a4a42 60%, #1a1a1a);
  }
  .featuring {
    position: absolute; left: 40px; top: 612px; width: 424px; text-align: right;
    font-family: "Arvo", serif; font-weight: 700; font-size: 31px; color: var(--ink);
  }
  .speaker-name {
    position: absolute; left: 58px; top: 660px; width: 420px; white-space: nowrap;
    font-family: "Montserrat", sans-serif; font-weight: 800; font-size: 35px; color: var(--charcoal);
  }
  .speaker-role {
    position: absolute; left: 60px; top: 705px; white-space: nowrap;
    font-family: "Arvo", serif; font-weight: 700; font-size: 28px; color: var(--ink);
  }
  .dates {
    position: absolute; left: 0; top: 788px; width: 436px; height: 153px;
    background: var(--white); border-radius: 0 76px 76px 0;
    padding: 16px 0 0 57px;
    font-family: "Arvo", serif; font-weight: 700; font-size: 34px; line-height: 40px; color: var(--green-deep);
  }
  .cost-ribbon { position: absolute; left: 438px; top: 784px; width: 352px; height: 162px; }
  .cost-text {
    position: absolute; left: 510px; top: 812px; width: 230px; text-align: center;
    font-family: "Montserrat", sans-serif; font-weight: 800; font-size: 21px; line-height: 26px; color: var(--white);
  }
  .childcare {
    position: absolute; left: 0; top: 962px; width: 570px; height: 57px;
    background: var(--green); padding: 20px 0 0 57px; white-space: nowrap;
    font-family: "Arvo", serif; font-weight: 700; font-size: 23px; color: var(--ink);
  }
  .details {
    position: absolute; left: 0; top: 1019px; width: 570px; height: 122px;
    background: var(--charcoal); padding: 18px 0 0 57px; white-space: nowrap;
    font-family: "Arvo", serif; font-weight: 700; font-size: 21.5px; line-height: 26px; color: var(--white);
  }
  .address {
    position: absolute; left: 0; top: 1141px; width: 570px; height: 59px;
    background: var(--green); padding: 14px 0 0 57px; white-space: nowrap;
    font-family: "Arvo", serif; font-weight: 700; font-size: 22px; color: var(--white);
  }
  .church-block {
    position: absolute; left: 570px; top: 962px; width: 230px; height: 238px;
    background: var(--charcoal);
    display: flex; align-items: center; justify-content: center; gap: 10px;
    padding-top: 40px;
  }
  .church-block .mark { width: 18px; height: 18px; background: var(--green); }
  .church-block .church-name {
    font-family: "Montserrat", sans-serif; font-weight: 700; font-size: 56px; color: var(--green);
  }
</style>
</head>
<body>
<main class="poster">
  <svg class="header-wave" viewBox="0 0 800 470" aria-hidden="true">
    <defs>
      <linearGradient id="sheen" x1="0" x2="1">
        <stop offset="0" stop-color="#ffffff" stop-opacity="0.2"/>
        <stop offset="0.6" stop-color="#ffffff" stop-opacity="0.9"/>
        <stop offset="1" stop-color="#ffffff" stop-opacity="0.1"/>
      </linearGradient>
    </defs>
    <path d="M0 0 H800 V206 C700 300 560 400 400 404 C240 408 110 360 0 305 Z" fill="#3a3a3c"/>
    <path d="M0 305 C110 360 240 408 400 404 C560 400 700 300 800 206 L800 225 C690 330 560 430 400 430 C240 430 110 380 0 325 Z" fill="url(#sheen)"/>
    <path d="M0 335 C130 395 260 440 420 445 C600 440 720 390 800 370 L800 380 C720 400 600 452 420 455 C260 452 130 405 0 345 Z" fill="#3a3a3c"/>
  </svg>

  <h1 class="headline">
    <span class="event-name">Rooted Lantern Conference:</span>
    <span class="tagline">Bridging the gap between<br>generations and passing<br>on our deepest beliefs<br>and values.</span>
  </h1>

  <div class="book-cover" role="img" aria-label="Cover of the book The Map of Q9"></div>
  <div class="speaker-photo" role="img" aria-label="Portrait photo of speaker Dr. Glen Marlowe"></div>

  <p class="featuring">Featuring</p>
  <p class="speaker-name">DR. GLEN MARLOWE.</p>
  <p class="speaker-role">Author of "The Map of Q9"</p>

  <div class="dates">Aug 25-26:<br>Friday 8-10 pm,<br>Saturday 4-8 pm</div>

  <svg class="cost-ribbon" viewBox="0 0 352 162" aria-hidden="true">
    <polygon points="300,40 340,150 290,120" fill="#1f78be"/>
    <polygon points="0,65 60,30 60,100" fill="#1f78be"/>
    <polygon points="55,12 300,22 325,140 60,125" fill="#2f9be0"/>
  </svg>
  <p class="cost-text">COST<br>ADULTS $15<br>CHILDREN $5</p>

  <p class="childcare">Childcare Provided For All Sessions.</p>
  <p class="details">Covers admission to all sessions and<br>workshops, refreshments and Saturday<br>dinner. *kids 5 and under free</p>
  <p class="address">4312 Orchard Bend, Cedar Hollow, TX 77512</p>

  <div class="church-block">
    <span class="mark"></span>
    <span class="church-name">orbc</span>
  </div>
</main>
</body>
</html>
```